brevakor.com

I have a site already disigned, however at the time I had no clue of how and what my site should look like. Still pretty cluless but I know I need to make some fundamenlal changes. I'm looking fora designer who understands how to connect with the cosumer with a ballance of visual and content with SEO in mind.I have a lot of content ready to be added to the mix, just missing alot of bottons for the content for example I have FAQ content but no FAQ botton. There are a lot of things I would like to add and take away from the current site. Here is a list of what I would like to add and subtracted from the site.Take away the find botton and ad contact us change the about botton to about brevakor,under that botton i want bottons that lead to News/Events,carreer opertunities,contact us and priacy policy. I also want to add Services offered: personal training,Motivational speeking ,bootcamp conditioning,rondalo,kickboxing cardio,and hip hop cordio. I want to add a botton for testimonials:video and written. I need to add a blog botton, a FAQ botton, and before and after. I want to add a social media botton: chatterloop, snapvelle,quibbler,hirenook,clipstream,and map corner. I need to add a store botton; T shirts. I would like the contact info the be linked to my email. and I would like would like at the top of contact form to read Request a free info session Now!!! But I don't need a new design I need to add these thing to the one I already have whitch is CMS based

Reason: I need my site to have new logo, just figured out how to down load logo

Reason: I need site to be CMS based so I can up load content and pics

Target Market(s)

People who want to loose weight, mostley women over the age of 30 and men over the age of 40 that income is at least 60,000 a year

Industry/Entity Type

Store

Font styles to use
Sans Serif
Decorative

Colors
000000
ec1f27
0255a3

Requirements
Must have
• Adding the drop downs listed above

```html
<!DOCTYPE html>
<html lang="en">
<head>
<meta charset="utf-8">
<title>brevakor fitness</title>
<link rel="stylesheet" href="https://fonts.googleapis.com/css2?family=Oswald:wght@400;500&family=Open+Sans:wght@400;600&display=swap">
<style>
:root{
  --red:#e21e26;
  --red-dark:#b8141b;
  --black:#0d0d0d;
  --navy:#111b29;
  --grey-band:#e7e7e7;
  --nav-bg:#ececec;
  --text:#555;
  --muted:#8a8a8a;
  --white:#fff;
}
*{box-sizing:border-box;margin:0;padding:0}
html,body{width:748px;height:1200px;overflow:hidden;background:var(--white)}
body{position:relative;font-family:"Open Sans",Arial,sans-serif;color:var(--text)}
.abs{position:absolute}
.heading{font-family:"Oswald",Arial,sans-serif;font-weight:400}

/* header */
.site-header{left:0;top:0;width:748px;height:174px;background:var(--white)}
.brand{left:0;top:70px;width:748px;display:flex;justify-content:center;align-items:center;gap:12px}
.brand-dot{width:34px;height:34px;border-radius:50%;background:var(--red)}
.brand-name{font-family:"Oswald",Arial,sans-serif;font-size:40px;font-weight:500;color:var(--black);line-height:1}

/* nav */
.main-nav{left:0;top:174px;width:748px;height:37px;background:var(--nav-bg);border-top:1px solid #ddd;border-bottom:1px solid #ddd}
.nav-list{left:22px;top:0;width:566px;height:35px;display:flex;justify-content:space-between;list-style:none}
.nav-item{position:relative;height:35px;padding-top:10px;font-size:10px;color:var(--muted);white-space:nowrap}
.nav-item.is-active{color:var(--red)}
.nav-item.is-active::after{content:"";position:absolute;left:-6px;right:-6px;bottom:-1px;height:3px;background:var(--red)}
.nav-item.has-menu::after{content:"";display:inline-block;margin-left:4px;vertical-align:2px;border-left:3px solid transparent;border-right:3px solid transparent;border-top:4px solid #a5a5a5}
.nav-item.is-open{color:var(--red)}
.nav-item.is-open::after{border-top-color:var(--red)}
.dropdown{left:-8px;top:36px;width:150px;list-style:none;background:var(--white);border-top:3px solid var(--red);box-shadow:0 3px 8px rgba(0,0,0,.25);z-index:5}
.dropdown li{height:25px;padding:6px 12px 0;font-size:10px;color:#666;border-bottom:1px solid #ececec}
.search-field{left:598px;top:183px;width:98px;height:22px;background:var(--white);border:1px solid #d6d6d6;font-size:10px;color:#aaa;padding:4px 6px}
.search-button{left:696px;top:183px;width:28px;height:22px;background:var(--red)}

/* hero */
.hero-photo{left:0;top:211px;width:748px;height:317px;background:linear-gradient(90deg,#7a4a30 0%,#b9784e 25%,#d9b79a 50%,#ece4da 70%,#f2eee8 100%)}
.contact-form{left:456px;top:227px;width:207px;height:283px;background:#f4f4f4;border:3px solid #e2e2e2;box-shadow:0 2px 6px rgba(0,0,0,.25)}
.form-title{left:0;top:0;width:201px;height:33px;background:var(--red);color:var(--white);font-size:13px;text-align:center;line-height:33px;white-space:nowrap}
.form-field{left:12px;width:177px;height:24px;background:var(--white);border:1px solid #d8d8d8;font-size:9px;color:#888;padding:6px 7px}
.form-select::after{content:"";position:absolute;right:-1px;top:-1px;width:15px;height:24px;background:#222}
.form-message{height:57px}
.form-submit{left:12px;top:238px;width:84px;height:24px;background:var(--red);color:var(--white);font-size:10px;text-align:center;line-height:24px}

/* promo band */
.promo-band{left:0;top:528px;width:748px;height:169px;background:var(--grey-band)}
.promo-card{top:25px;width:306px;height:119px;background:var(--navy);border:1px solid #6a7380}
.promo-photo{left:4px;top:4px;width:114px;height:109px}
.promo-title{left:128px;top:14px;font-size:27px;color:var(--white);line-height:1.1}
.promo-text{left:128px;top:56px;width:165px;font-size:10px;line-height:1.35;color:#8e98a8}

/* news / events / careers */
.section-title{font-size:21px;color:var(--red);line-height:1}
.post{width:170px;height:64px}
.post-thumb{left:0;top:0;width:63px;height:51px}
.post-date{left:75px;top:-1px;font-size:11px;color:#444}
.post-text{left:75px;top:15px;width:100px;font-size:9px;line-height:1.35;color:var(--muted)}
.post-divider{height:1px;background:#e4e4e4}
.career-photo{left:471px;top:762px;width:212px;height:91px;background:linear-gradient(90deg,#1c1c1c,#5a3a28 55%,#222)}
.career-caption{left:471px;top:853px;width:212px;height:43px;background:var(--red);color:var(--white);font-size:9px;line-height:1.4;padding:5px 9px}

/* dark section */
.dark-band{left:0;top:920px;width:748px;height:221px;background:linear-gradient(90deg,#0a0a0a,#1d1d1d 50%,#0a0a0a)}
.dark-title{font-size:20px;color:var(--white);line-height:1}
.service-list{left:60px;top:982px;width:130px;list-style:none}
.service-list li{height:24px;border-bottom:1px solid #2e2e2e;font-size:10px;color:#aaa;padding-top:5px;padding-left:12px;position:relative}
.service-list li::before{content:"";position:absolute;left:0;top:10px;width:4px;height:4px;background:#ccc}
.service-list li.is-active{color:var(--red)}
.testimonial-card{left:222px;top:983px;width:195px;height:134px;background:var(--white);border:3px solid #cfcfcf;padding:9px 12px 0 20px}
.testimonial-text{font-size:9px;line-height:1.35;color:#999;font-style:italic}
.testimonial-quote{font-family:Georgia,serif;font-size:22px;color:#bbb;line-height:1}
.testimonial-meta{left:20px;top:112px;width:160px;font-size:9px;color:var(--red);display:flex;justify-content:space-between}
.video-frame{left:449px;top:983px;width:236px;height:134px;background:#222;border:3px solid #ccc}
.video-photo{left:0;top:0;width:230px;height:128px;background:linear-gradient(90deg,#2a1d17,#7a4c33 50%,#2a1d17)}
.play-button{left:93px;top:49px;width:44px;height:30px;background:var(--red);border-radius:6px}

/* footer */
.site-footer{left:0;top:1141px;width:748px;height:59px;background:var(--red)}
.social-link{top:12px;width:18px;height:18px;background:var(--white);border-radius:2px}
.footer-copy{left:0;top:40px;width:748px;text-align:center;font-size:8px;color:var(--white);letter-spacing:.2px}
</style>
</head>
<body>

<header class="site-header abs">
  <div class="brand abs">
    <span class="brand-dot"></span>
    <span class="brand-name">brevakor</span>
  </div>
</header>

<section class="hero">
  <div class="hero-photo abs" role="img" aria-label="Muscular man flexing in front of a white brick wall"></div>
  <form class="contact-form abs">
    <div class="form-title heading abs">Request a free info session Now!!!</div>
    <div class="form-field form-select abs" style="top:52px">Choose Program</div>
    <div class="form-field abs" style="top:84px">Date</div>
    <div class="form-field form-select abs" style="top:116px">Number of Persons</div>
    <div class="form-field abs" style="top:146px">E-Mail</div>
    <div class="form-field form-message abs" style="top:173px">Message</div>
    <div class="form-submit abs">Book Now</div>
  </form>
</section>

<nav class="main-nav abs">
  <ul class="nav-list abs">
    <li class="nav-item is-active">Home</li>
    <li class="nav-item has-menu is-open">About brevakor
      <ul class="dropdown abs">
        <li>News / Events</li>
        <li>Carreer Opertunities</li>
        <li>Contact Us</li>
        <li>Privacy Policy</li>
      </ul>
    </li>
    <li class="nav-item has-menu">Services</li>
    <li class="nav-item has-menu">Testimonials</li>
    <li class="nav-item">Blog</li>
    <li class="nav-item">FAQ</li>
    <li class="nav-item">Before &amp; After</li>
    <li class="nav-item has-menu">Social Media</li>
    <li class="nav-item has-menu">Store</li>
    <li class="nav-item">Contact Us</li>
  </ul>
</nav>
<div class="search-field abs">Search</div>
<div class="search-button abs">
  <svg width="28" height="22" viewBox="0 0 28 22"><circle cx="13" cy="10" r="4.5" fill="none" stroke="#fff" stroke-width="2"/><line x1="16.2" y1="13.2" x2="19.5" y2="16.5" stroke="#fff" stroke-width="2.2" stroke-linecap="round"/></svg>
</div>

<section class="promo-band abs">
  <article class="promo-card abs" style="left:62px">
    <div class="promo-photo abs" role="img" aria-label="Arm lifting a dumbbell" style="background:linear-gradient(135deg,#c9d2dc,#6b4a36 60%,#2a2f38)"></div>
    <h3 class="promo-title heading abs">Tips and Advice</h3>
    <p class="promo-text abs">Fierfors Veyaside kytraserta citrasisaas caetsa maserte tirldas dolore nuyas vuytsas.</p>
  </article>
  <article class="promo-card abs" style="left:380px">
    <div class="promo-photo abs" role="img" aria-label="Muscular torso with dog tags" style="background:linear-gradient(135deg,#3a2a20,#a06a48 55%,#3a2a20)"></div>
    <h3 class="promo-title heading abs">For Advanced</h3>
    <p class="promo-text abs">yaside kytraserta Fiertersade tisa maserte tirldas scitras lisaserae nuaysras yas dasa.</p>
  </article>
</section>

<section class="updates">
  <h2 class="section-title heading abs" style="left:62px;top:722px">News</h2>
  <div class="post abs" style="left:63px;top:762px">
    <div class="post-thumb abs" role="img" aria-label="Woman training with a dumbbell" style="background:linear-gradient(135deg,#ddd,#9a7a66)"></div>
    <span class="post-date abs">July 05, 2014</span>
    <p class="post-text abs">Lorem quis, lobortis dignissim, pulvinar ac</p>
  </div>
  <div class="post-divider abs" style="left:63px;top:825px;width:170px"></div>
  <div class="post abs" style="left:63px;top:842px">
    <div class="post-thumb abs" role="img" aria-label="Athlete posing" style="background:linear-gradient(135deg,#bbb,#5e4538)"></div>
    <span class="post-date abs">July 05, 2014</span>
    <p class="post-text abs">Lorem quis, lobortis dignissim, pulvinar ac</p>
  </div>

  <h2 class="section-title heading abs" style="left:262px;top:722px">Events</h2>
  <div class="post abs" style="left:263px;top:762px">
    <div class="post-thumb abs" role="img" aria-label="Bodybuilder posing on dark background" style="background:linear-gradient(135deg,#111,#7a5238)"></div>
    <span class="post-date abs">July 05, 2014</span>
    <p class="post-text abs">Lorem quis, lobortis dignissim, pulvinar ac</p>
  </div>
  <div class="post-divider abs" style="left:263px;top:825px;width:170px"></div>
  <div class="post abs" style="left:263px;top:842px">
    <div class="post-thumb abs" role="img" aria-label="Athlete doing push-ups" style="background:linear-gradient(135deg,#111,#666)"></div>
    <span class="post-date abs">July 05, 2014</span>
    <p class="post-text abs">Lorem quis, lobortis dignissim, pulvinar ac</p>
  </div>

  <h2 class="section-title heading abs" style="left:469px;top:722px">Carreer Opertunities</h2>
  <div class="career-photo abs" role="img" aria-label="Athlete lifting dumbbells, seen from behind"></div>
  <p class="career-caption abs">Lorem ipsum dolor sit amet, consectetuer adipiscing elit, sed diam nonummy nibh volutpat.</p>
</section>

<section class="dark-band abs">
  <h2 class="dark-title heading abs" style="left:62px;top:34px">Services</h2>
  <h2 class="dark-title heading abs" style="left:222px;top:34px">Testimonials</h2>
  <h2 class="dark-title heading abs" style="left:449px;top:34px">Videos</h2>
</section>
<ul class="service-list abs">
  <li class="is-active">Personal Training</li>
  <li>Motivational Speeking</li>
  <li>Bootcamp Conditioning</li>
  <li>Rondalo</li>
  <li>Kickboxing Cardio</li>
  <li>Hip Hop Cordio</li>
</ul>
<div class="testimonial-card abs">
  <p class="testimonial-text"><span class="testimonial-quote">“</span> Lorem ipsum dolor sit amet, consectetuer adipiscing elit, sed diam nonummy nibh euismod tincidunt ut laoreet dolore magna aliquam erat volutpat. Ut wisi enim ad minim veniam, quis nostrud exerci tation ullamcorper.</p>
  <div class="testimonial-meta abs"><span>- Lorem Ipsum</span><span>Read More</span></div>
</div>
<div class="video-frame abs">
  <div class="video-photo abs" role="img" aria-label="Man training with dumbbells in a gym"></div>
  <div class="play-button abs">
    <svg width="44" height="30" viewBox="0 0 44 30"><polygon points="17,8 29,15 17,22" fill="#fff"/></svg>
  </div>
</div>

<footer class="site-footer abs">
  <span class="social-link abs" style="left:320px" aria-label="chatterloop"></span>
  <span class="social-link abs" style="left:342px" aria-label="quibbler"></span>
  <span class="social-link abs" style="left:364px" aria-label="hirenook"></span>
  <span class="social-link abs" style="left:386px" aria-label="clipstream"></span>
  <span class="social-link abs" style="left:408px" aria-label="snapvelle"></span>
  <p class="footer-copy abs">BREVAKOR © 2014 PRIVACY POLICY. ALL RIGHTS RESERVED.</p>
</footer>

</body>
</html>
```